Science News Webpage Design

Quarry Lantern Works gGmbH is a non-profit organisation developing apps for scientists. Our main project is a scientific platform you can visit at quarrylantern.net.

The QLW platform consists of multiple modules. We are now considering to spin out one of the modules (Tides & Notes) and create a separate web application with focus on latest science news that enables scientists to easily contribute by writing their own articles and commentaries.

For this news website, we need someone to design the homepage and three other templates.

We prepared a set of files consisting of a more detailed brief and also a couple of wire-frames.

Please check these files and get in touch with us in case you have questions or in case something is unclear.
Updates

Hello everyone,

Just a short note. Although I have indicated in the brief that this project is a spin-out from another platform, you shouldn't feel restricted to design and color combinations of that other site. We are really trying to make something new here, and the design can be completely different.

I also attached a new file. The working title of the project is "wonder unwrapped". Although we haven't decided on the final name, you can use this png as logo.

Cheers,
Toma

Updated home page wireframe to include all links in the menu (since there are more links than originally depicted and this obviously influences design).

Industry/Entity Type

Non-Profit

```html
<!DOCTYPE html>
<html lang="en">
<head>
<meta charset="utf-8">
<title>wonder unwrapped – Science, Health &amp; Technology News</title>
<link href="https://fonts.googleapis.com/css2?family=Roboto:wght@400;500;700;900&display=swap" rel="stylesheet">
<style>
:root{
  --orange:#e4581d;
  --orange-dark:#c8460f;
  --ink:#2b2b2b;
  --muted:#6b6b6b;
  --line:#e2e2e2;
  --dark:#3a3a3a;
  --footer:#454545;
  --white:#ffffff;
  --teal:#19a6a0;
  --navy:#123d80;
  --sky:#cfe8f6;
  --gold:#ffd23f;
}
*{box-sizing:border-box;margin:0;padding:0}
html,body{width:1200px;height:3688px;overflow:hidden}
body{font-family:"Roboto",Arial,sans-serif;color:var(--ink);position:relative;background:#dfe9f2}
.backdrop{position:absolute;inset:0;background:
  radial-gradient(circle at 6% 4%,#1f5d98 0,#5f95c4 14%,transparent 34%),
  radial-gradient(circle at 96% 6%,#2f70aa 0,#8fb7da 16%,transparent 36%),
  radial-gradient(ellipse at 3% 60%,#b9d2e8 0,transparent 30%),
  linear-gradient(180deg,#b9d3ea 0,#e3edf6 28%,#eef3f8 100%)}
.page{position:absolute;left:57px;top:22px;width:1086px;height:3547px;background:var(--white)}

/* image fills: soft gradients in each scene's tones */
.fill{display:block;width:100%;position:relative;overflow:hidden;box-shadow:inset 0 0 0 1px rgba(0,0,0,.06)}
.fill::after{content:"";position:absolute;inset:0;background:linear-gradient(180deg,rgba(255,255,255,.12),rgba(0,0,0,.08))}
.f-bacteria{background:radial-gradient(ellipse 30% 18% at 30% 30%,#efefef,transparent 70%),radial-gradient(ellipse 26% 14% at 66% 22%,#e2e2e2,transparent 70%),radial-gradient(ellipse 34% 20% at 55% 60%,#d6d6d6,transparent 70%),radial-gradient(ellipse 20% 12% at 18% 70%,#cfcfcf,transparent 70%),linear-gradient(160deg,#8d8d8d,#4b4b4b 60%,#2e2e2e)}
.f-seedling{background:radial-gradient(circle at 62% 45%,#7fb241 0,#a8cf6a 18%,transparent 38%),radial-gradient(circle at 30% 55%,#e7eaee 0,transparent 40%),linear-gradient(135deg,#f4f5f6,#dfe6df 55%,#f1f1f1)}
.f-chem{background:radial-gradient(ellipse 14% 40% at 78% 50%,#d23a26,transparent 70%),radial-gradient(circle at 35% 45%,#e9cbb1,transparent 40%),linear-gradient(120deg,#efe4d9,#cfb7a2 45%,#f5ebe2)}
.f-skyline{background:radial-gradient(ellipse 60% 30% at 50% 92%,#f3a04a,transparent 70%),linear-gradient(180deg,#1d3c77 0,#3e64a4 45%,#7a7fa8 62%,#b77a4e 78%,#40384a 100%)}
.f-poster{background:linear-gradient(180deg,#f0f2ea 0,#f0f2ea 30%,#3f7d4c 31%,#6aa36a 60%,#d6e2c8 61%,#e8eee0 100%)}
.f-career{background:radial-gradient(circle at 70% 40%,#c8c8c8,transparent 45%),linear-gradient(160deg,#6e6e6e,#3e3e3e 60%,#8f8f8f)}
.f-cluster{background:linear-gradient(180deg,#ffffff 0,#ffffff 30%,#e23b2f 31%,#e23b2f 33%,#f6f6f6 34%,#dfe3e6 100%)}
.f-cradle{background:radial-gradient(circle at 22% 62%,#cfe6c2,transparent 16%),radial-gradient(circle at 40% 62%,#bcd9ae,transparent 16%),radial-gradient(circle at 58% 62%,#a9cf98,transparent 16%),radial-gradient(circle at 76% 62%,#7fb35e,transparent 16%),linear-gradient(180deg,#f6f6f6,#e2e6e2)}
.f-calc{background:radial-gradient(ellipse 30% 30% at 70% 65%,#9aa3aa,transparent 70%),radial-gradient(ellipse 30% 24% at 62% 25%,#e9cdb6,transparent 70%),linear-gradient(135deg,#fafafa,#e1e4e7 60%,#f3f3f3)}
.f-earth{background:radial-gradient(circle at 45% 52%,#3f86c9 0,#6aa7dc 14%,transparent 22%),linear-gradient(180deg,#5f9fd8 0,#b9d8f1 50%,#8cc55a 66%,#4f9a2f 100%)}
.f-tech{background:radial-gradient(circle at 30% 40%,#7fc4ff,transparent 30%),radial-gradient(circle at 75% 55%,#4d8fd6,transparent 30%),linear-gradient(135deg,#07152c,#1b4f8d 55%,#061022)}
.f-health{background:radial-gradient(ellipse 30% 40% at 35% 50%,#6ea5d8,transparent 70%),radial-gradient(ellipse 24% 34% at 72% 45%,#e9d4c6,transparent 70%),linear-gradient(135deg,#e8f0f6,#b9cde0 55%,#f1f4f7)}
.f-social{background:radial-gradient(ellipse 22% 18% at 70% 70%,#e2574a,transparent 70%),radial-gradient(ellipse 30% 20% at 35% 30%,#cfcfcf,transparent 70%),linear-gradient(135deg,#fbfbfb,#e6e6e6)}
.f-tree{background:radial-gradient(circle at 25% 35%,#f3a23c,transparent 18%),radial-gradient(circle at 55% 25%,#e4581d,transparent 16%),radial-gradient(circle at 78% 40%,#4aa0d0,transparent 18%),radial-gradient(circle at 45% 55%,#8cc152,transparent 18%),radial-gradient(ellipse 8% 30% at 50% 85%,#7a4a2a,transparent 70%),linear-gradient(180deg,#fff,#f6efe8)}
.f-lab{background:radial-gradient(ellipse 20% 35% at 30% 55%,#9fb8cc,transparent 70%),radial-gradient(ellipse 16% 28% at 70% 58%,#c9d6df,transparent 70%),linear-gradient(180deg,#fbfbfb,#e4e9ed)}
.f-cells{background:radial-gradient(circle at 25% 30%,#ff5fa2,transparent 25%),radial-gradient(circle at 70% 65%,#3a7bff,transparent 30%),radial-gradient(circle at 60% 20%,#b44cff,transparent 25%),linear-gradient(135deg,#3b0f55,#8b1f7c 50%,#1c3f9a)}
.f-worm{background:radial-gradient(ellipse 40% 30% at 55% 55%,#d8d8d8,transparent 70%),radial-gradient(circle at 50% 50%,#9a9a9a,#3c3c3c 80%)}
.f-beetle{background:radial-gradient(ellipse 26% 18% at 50% 55%,#7a4a1e,transparent 75%),radial-gradient(circle at 30% 30%,#f6e3bb,transparent 40%),linear-gradient(135deg,#efd9a9,#c08a3f 55%,#f1dfb6)}
.t-grey{background:radial-gradient(ellipse 40% 20% at 40% 40%,#efefef,transparent 70%),linear-gradient(160deg,#8a8a8a,#3d3d3d)}
.t-insect{background:radial-gradient(ellipse 30% 20% at 50% 55%,#6e4a1c,transparent 75%),linear-gradient(135deg,#f0d79c,#a8782e)}
.t-red{background:radial-gradient(circle at 55% 50%,#ff8a6a,transparent 40%),linear-gradient(135deg,#c44a2c,#6b1a10)}
.t-bench{background:radial-gradient(ellipse 30% 40% at 50% 45%,#e8d6cc,transparent 70%),linear-gradient(135deg,#d6cbc6,#7a6a64)}

/* top ad */
.top-ad{position:absolute;left:213px;top:18px;width:666px;height:90px;display:flex;border:1px solid #d6e6c8;overflow:hidden}
.top-ad .brand{width:170px;background:linear-gradient(180deg,#fff,#e6f1fb);display:flex;flex-direction:column;justify-content:center;align-items:center;font-weight:900;color:#1f5fa8;font-size:25px;letter-spacing:-.5px}
.top-ad .brand small{font-size:11px;color:var(--orange);letter-spacing:1px;font-weight:900}
.top-ad .pitch{flex:1;background:linear-gradient(180deg,#2f8fd1,#1d6bb0);color:#fff;display:flex;flex-direction:column;justify-content:center;padding:0 14px}
.top-ad .pitch b{font-size:20px;line-height:1.08;font-weight:900;color:#fff7b0}
.top-ad .pitch span{font-size:10.5px;background:#6fb03a;margin-top:6px;padding:3px 6px;font-weight:500}
.top-ad .guide{width:150px;background:#eaf5fb;color:#1d6bb0;font-size:12px;font-weight:700;text-align:center;display:flex;flex-direction:column;justify-content:center;align-items:center;gap:6px;padding:0 8px;line-height:1.2}
.top-ad .guide em{font-style:normal;background:var(--orange);color:#fff;padding:4px 12px;border-radius:10px;font-size:11px;font-weight:900}

/* header */
.site-head{position:absolute;left:20px;top:135px;width:1046px;height:80px}
.logo{font-size:38px;font-weight:700;color:var(--ink);letter-spacing:-1px;line-height:1;display:flex;align-items:center;gap:8px;margin-top:12px}
.logo i{width:12px;height:12px;border-radius:50%;background:var(--orange);display:block}
.tagline{font-size:13px;color:var(--muted);margin-top:4px}
.account{position:absolute;right:140px;top:12px;display:flex;align-items:center;gap:6px;font-size:10px;color:var(--muted)}
.btn-dark{background:var(--dark);color:#fff;font-size:10px;font-weight:700;padding:6px 8px;text-transform:uppercase;display:inline-block}
.socials{position:absolute;right:0;top:8px;display:flex;gap:6px}
.socials span{width:28px;height:28px;display:block;border-radius:3px}
.search{position:absolute;right:0;top:54px;width:238px;height:24px;border:1px solid var(--line);display:flex}
.search span{flex:1;font-size:11px;color:#aaa;padding:5px 8px}
.search b{width:26px;background:var(--ink);display:flex;align-items:center;justify-content:center}

/* nav */
.nav{position:absolute;left:-11px;top:228px;width:1108px;height:40px;background:var(--orange);display:flex;align-items:center;padding:0 18px;justify-content:space-between;box-shadow:0 2px 3px rgba(0,0,0,.2)}
.nav a{color:#fff;font-size:13px;font-weight:500;text-decoration:none;padding:0 8px;text-transform:uppercase}

/* hero */
.hero-row{position:absolute;left:20px;top:282px;width:1046px;display:flex;gap:26px}
.hero{width:749px;height:386px;position:relative}
.hero .arrow{position:absolute;top:140px;width:28px;height:28px;border-radius:50%;background:rgba(255,255,255,.9);display:flex;align-items:center;justify-content:center;z-index:2}
.hero .caption{position:absolute;left:0;bottom:0;width:100%;height:126px;background:rgba(0,0,0,.66);color:#fff;padding:34px 14px 0;z-index:2}
.hero .label{position:absolute;left:0;top:-20px;background:var(--orange);color:#fff;font-weight:700;font-size:15px;padding:10px 14px}
.hero h1{font-size:24px;font-weight:500;margin-bottom:8px}
.hero p{font-size:12px;line-height:1.4;color:#ddd}
.hero p a{color:var(--orange)}
.sidebar{width:275px}
.signup{border:1px solid var(--line);padding:12px 14px;height:114px}
.signup h3{color:var(--orange);font-size:19px;font-weight:500;margin-bottom:6px}
.signup p{font-size:11px;color:var(--muted);margin-bottom:10px}
.promo{margin-top:22px;height:232px;background:radial-gradient(circle at 50% 70%,#3d3d3d,#1c1c1c 70%);color:#fff;padding:14px;display:flex;flex-direction:column;align-items:center}
.promo .brand{font-size:16px;font-weight:700;display:flex;align-items:center;gap:6px;align-self:flex-start}
.promo .brand i{width:14px;height:14px;border-radius:50%;background:#fff;display:block}
.promo p{font-size:15px;font-weight:700;text-align:center;margin:8px 0;line-height:1.25}
.promo .shirt{width:118px;height:88px}
.promo .cta{margin-top:10px;background:var(--teal);padding:7px 22px;font-size:12px;font-weight:700}

/* section grid */
.row{position:absolute;left:20px;width:1046px;display:grid;grid-template-columns:334px 330px 312px;column-gap:35px}
.card{border:1px solid var(--line);border-top:none;padding:0 0 10px;height:100%;box-shadow:0 2px 3px rgba(0,0,0,.05)}
.card-head{display:flex;justify-content:space-between;align-items:center;height:44px;border-bottom:1px solid var(--line);padding:0 10px}
.card-head h2{color:var(--orange);font-size:17px;font-weight:700;text-transform:uppercase}
.see-all{background:var(--dark);color:#fff;font-size:9px;font-weight:700;padding:7px 8px}
.card .body{padding:12px 10px 0}
.lead h3{font-size:15px;font-weight:500;line-height:1.35;margin:10px 0 6px}
.meta{font-size:10.5px;color:var(--orange)}
.item{border:1px solid var(--line);padding:10px 12px;margin-top:12px;box-shadow:0 1px 2px rgba(0,0,0,.06)}
.item p{font-size:12.5px;line-height:1.4;margin-bottom:6px}
.mini{display:flex;gap:10px;border:1px solid var(--line);padding:8px;margin-top:10px;height:108px;box-shadow:0 1px 2px rgba(0,0,0,.06)}
.mini .thumb{width:68px;height:62px;flex:none}
.mini p{font-size:12px;line-height:1.35;margin-bottom:5px}

/* bands */
.band{position:absolute;left:-11px;width:1108px;background:var(--orange);padding:14px 31px 0;box-shadow:0 3px 6px rgba(0,0,0,.25)}
.band-head{display:flex;justify-content:space-between;align-items:center;color:#fff;font-weight:700;font-size:17px;height:34px}
.band-head .arrows{display:flex;gap:14px}
.band-cards{display:grid;grid-template-columns:repeat(4,240px);column-gap:30px;margin-top:12px;position:relative}
.band-card h3{color:#fff;font-size:14px;font-weight:700;line-height:1.35;margin:12px 0 10px;height:58px}
.band-card .strip{background:#fff;margin:0 -6px;padding:6px}
.band-card .strip .meta{color:var(--ink)}
.band-strip{position:absolute;left:0;right:0;bottom:0;height:28px;background:#fff}

/* ads */
.ad-host{height:238px;background:radial-gradient(circle at 80% 30%,#2a67bd,transparent 50%),linear-gradient(180deg,#1b4f9c,#0e2f6a);color:#fff;padding:16px;position:relative}
.ad-host h4{font-size:17px;font-weight:900;line-height:1.2}
.ad-host h4 span{color:var(--gold)}
.ad-host ul{list-style:none;margin-top:12px;font-size:11px;font-weight:700;line-height:1.9}
.ad-host li::before{content:"";display:inline-block;width:6px;height:6px;background:var(--gold);margin-right:6px;vertical-align:middle}
.ad-host .art{position:absolute;right:14px;top:58px;width:104px;height:112px;border-radius:50% 50% 40% 40%;background:radial-gradient(circle at 40% 35%,#ffd36b,#e8951f 60%,#b86a10)}
.ad-host .from{position:absolute;right:16px;bottom:42px;font-size:10px;font-weight:700}
.ad-host .price{position:absolute;right:16px;bottom:12px;font-size:26px;font-weight:900;color:var(--gold)}
.ad-host .click{position:absolute;left:16px;bottom:16px;background:var(--gold);color:#0e2f6a;font-size:11px;font-weight:900;padding:6px 12px;border-radius:3px}
.ad-gig{height:232px;margin-top:18px;background:linear-gradient(180deg,#e8f5fc,#bfe2f3);padding:16px;position:relative;color:var(--navy);overflow:hidden}
.ad-gig h4{font-size:22px;font-weight:900;line-height:1.1;width:140px}
.ad-gig h4 span{color:var(--orange)}
.ad-gig .person{position:absolute;right:10px;top:34px;width:124px;height:150px;border-radius:60px 60px 6px 6px;background:linear-gradient(180deg,#d9eefa,#7fb3d6)}
.ad-gig .tag{position:absolute;right:0;top:10px;background:var(--orange);color:#fff;font-size:11px;font-weight:700;padding:3px 10px}
.ad-gig .brand{position:absolute;left:0;right:0;bottom:0;height:40px;background:#fff;padding:0 16px;font-size:18px;font-weight:700;display:flex;align-items:center;gap:6px}
.ad-gig .brand i{width:12px;height:12px;background:var(--navy);display:block}

/* footer */
.footer{position:absolute;left:0;top:3569px;width:1200px;height:119px;background:var(--footer);color:#ccc;text-align:center;padding-top:28px}
.footer nav{font-size:11px;color:#fff;display:flex;justify-content:center;gap:10px}
.footer nav span{color:#999}
.footer p{font-size:10px;margin-top:10px;line-height:1.6}
</style>
</head>
<body>
<div class="backdrop" role="img" aria-label="Blurred laboratory glassware in blue light"></div>

<div class="page">
  <aside class="top-ad">
    <div class="brand">Brightlaunch<small>GET GOING!</small></div>
    <div class="pitch"><b>START YOUR DREAM<br>BUSINESS TODAY!</b><span>Plan, Fund and Start a New Business with Your 10-Step Startup Roadmap</span></div>
    <div class="guide">FREE Guide to Starting Your Own Business<em>GET GOING!</em></div>
  </aside>

  <header class="site-head">
    <div class="logo"><i></i>wonder unwrapped</div>
    <div class="tagline">Science, Health &amp; Technology News</div>
    <div class="account"><span class="btn-dark">Sign in</span>or<span class="btn-dark">Sign up</span></div>
    <div class="socials"><span style="background:#3b5998"></span><span style="background:#29a9e1"></span><span style="background:#0e76a8"></span><span style="background:#dd4b39"></span></div>
    <div class="search"><span>Search...</span><b><svg width="12" height="12" viewBox="0 0 12 12"><circle cx="5" cy="5" r="3.5" fill="none" stroke="#fff" stroke-width="1.5"/><line x1="7.6" y1="7.6" x2="11" y2="11" stroke="#fff" stroke-width="1.5"/></svg></b></div>
  </header>

  <nav class="nav">
    <a>Home</a><a>Latest</a><a>Biology</a><a>Chemistry</a><a>Physics</a><a>Computation</a><a>Technology</a><a>Health</a><a>Social</a><a>More News</a><a>Questions?</a>
  </nav>

  <section class="hero-row">
    <div class="hero fill f-bacteria" role="img" aria-label="Microscope image of rod-shaped tuberculosis bacteria">
      <span class="arrow" style="left:12px"><svg width="10" height="10" viewBox="0 0 10 10"><path d="M7 1 3 5l4 4" fill="none" stroke="#333" stroke-width="2"/></svg></span>
      <span class="arrow" style="right:12px"><svg width="10" height="10" viewBox="0 0 10 10"><path d="M3 1l4 4-4 4" fill="none" stroke="#333" stroke-width="2"/></svg></span>
      <div class="caption">
        <span class="label">LATEST NEWS</span>
        <h1>Tuberculosis test on its way</h1>
        <p>Childhood tuberculosis accounts for 10% of cases world wide. A new test might get results faster, allowing better treatment and outcome... <a>Read More</a></p>
      </div>
    </div>
    <div class="sidebar">
      <div class="signup">
        <h3>SIGN UP</h3>
        <p>To upload articles, bookmark, comments...</p>
        <span class="btn-dark">Find out more</span>
      </div>
      <aside class="promo">
        <div class="brand"><i></i>Stackmint</div>
        <p>Stackmint &amp; Codewell teamed up to offer this custom shirt!</p>
        <svg class="shirt" viewBox="0 0 118 88" role="img" aria-label="Dark t-shirt with a tools emblem"><path d="M38 4 18 12 4 32l16 10 6-6v50h66V36l6 6 16-10-14-20-20-8c-4 8-12 12-21 12S42 12 38 4z" fill="#4a4a4a"/></svg>
        <span class="cta">Get it now</span>
      </aside>
    </div>
  </section>

  <!-- row 1 -->
  <section class="row" style="top:688px;height:515px">
    <article class="card"><div class="card-head"><h2>Biology</h2><span class="see-all">SEE ALL</span></div><div class="body">
      <div class="fill f-seedling" style="height:140px" role="img" aria-label="Scientist tending a seedling in a lab"></div>
      <div class="lead"><h3>Lorem ipsum dolor sit amet, consectetur adipiscing elit risus in magna varius commodo.</h3><div class="meta">Genetic Engineering | Article | By J.Smith</div></div>
      <div class="item"><p>Lorem ipsum dolor sit amet, consectetur adipiscing elit risus in magna varius commodo.</p><div class="meta">Genetic Engineering | Article | By J.Smith</div></div>
      <div class="item"><p>Lorem ipsum dolor sit amet, consectetur adipiscing elit risus in magna varius commodo.</p><div class="meta">Genetic Engineering | Article | By J.Smith</div></div>
    </div></article>
    <article class="card"><div class="card-head"><h2>Chemistry</h2><span class="see-all">SEE ALL</span></div><div class="body">
      <div class="fill f-chem" style="height:140px" role="img" aria-label="Chemist holding a test tube of red liquid"></div>
      <div class="lead"><h3>Lorem ipsum dolor sit amet, consectetur adipiscing elit risus in magna varius commodo.</h3><div class="meta">Genetic Engineering | Article | By J.Smith</div></div>
      <div class="item"><p>Lorem ipsum dolor sit amet, consectetur adipiscing elit risus in magna varius commodo.</p><div class="meta">Genetic Engineering | Article | By J.Smith</div></div>
      <div class="item"><p>Lorem ipsum dolor sit amet, consectetur adipiscing elit risus in magna varius commodo.</p><div class="meta">Genetic Engineering | Article | By J.Smith</div></div>
    </div></article>
    <article class="card"><div class="card-head"><h2>Most Popular</h2><span class="see-all">SEE ALL</span></div><div class="body">
      <div class="mini"><div class="thumb fill t-grey" role="img" aria-label="Grey bacteria close-up"></div><div><p>Lorem ipsum dolor sit amet, consectetur adipiscing elit risus in magna...</p><div class="meta">Genetic Engineering | Article</div></div></div>
      <div class="mini"><div class="thumb fill t-insect" role="img" aria-label="Insect on a leaf"></div><div><p>Lorem ipsum dolor sit amet, consectetur adipiscing elit risus in magna...</p><div class="meta">Genetic Engineering | Article</div></div></div>
      <div class="mini"><div class="thumb fill t-red" role="img" aria-label="Red laboratory sample"></div><div><p>Lorem ipsum dolor sit amet, consectetur adipiscing elit risus in magna...</p><div class="meta">Genetic Engineering | Article</div></div></div>
      <div class="mini"><div class="thumb fill t-bench" role="img" aria-label="Researcher at a bench"></div><div><p>Lorem ipsum dolor sit amet, consectetur adipiscing elit risus in magna...</p><div class="meta">Genetic Engineering | Article</div></div></div>
    </div></article>
  </section>

  <!-- sponsored -->
  <section class="band" style="top:1229px;height:315px">
    <div class="band-strip"></div>
    <div class="band-head"><span>SPONSORED</span><span class="arrows"><svg width="8" height="10" viewBox="0 0 8 10"><path d="M6 1 2 5l4 4" fill="none" stroke="#fff" stroke-width="2"/></svg><svg width="8" height="10" viewBox="0 0 8 10"><path d="M2 1l4 4-4 4" fill="none" stroke="#fff" stroke-width="2"/></svg></span></div>
    <div class="band-cards">
      <div class="band-card"><div class="fill f-skyline" style="height:138px" role="img" aria-label="City skyline at dusk"></div><h3>Lorem ipsum dolor sit amet, consectetur adipiscing elit risus in magna varius commodo.</h3><div class="strip"><div class="meta">Genetic Engineering | Article | By J.Smith</div></div></div>
      <div class="band-card"><div class="fill f-poster" style="height:138px" role="img" aria-label="Conference poster for a bio competition"></div><h3>Lorem ipsum dolor sit amet, consectetur adipiscing elit risus in magna varius commodo.</h3><div class="strip"><div class="meta">Genetic Engineering | Article | By J.Smith</div></div></div>
      <div class="band-card"><div class="fill f-career" style="height:138px" role="img" aria-label="Poster for a science communication career day"></div><h3>Lorem ipsum dolor sit amet, consectetur adipiscing elit risus in magna varius commodo.</h3><div class="strip"><div class="meta">Genetic Engineering | Article | By J.Smith</div></div></div>
      <div class="band-card"><div class="fill f-cluster" style="height:138px" role="img" aria-label="Biomedical cluster banner"></div><h3>Lorem ipsum dolor sit amet, consectetur adipiscing elit risus in magna varius commodo.</h3><div class="strip"><div class="meta">Genetic Engineering | Article | By J.Smith</div></div></div>
    </div>
  </section>

  <!-- row 2 -->
  <section class="row" style="top:1567px;height:525px">
    <article class="card"><div class="card-head"><h2>Physics</h2><span class="see-all">SEE ALL</span></div><div class="body">
      <div class="fill f-cradle" style="height:140px" role="img" aria-label="Newton's cradle with glass spheres"></div>
      <div class="lead"><h3>Lorem ipsum dolor sit amet, consectetur adipiscing elit risus in magna varius commodo.</h3><div class="meta">Genetic Engineering | Article | By J.Smith</div></div>
      <div class="item"><p>Lorem ipsum dolor sit amet, consectetur adipiscing elit risus in magna varius commodo.</p><div class="meta">Genetic Engineering | Article | By J.Smith</div></div>
      <div class="item"><p>Lorem ipsum dolor sit amet, consectetur adipiscing elit risus in magna varius commodo.</p><div class="meta">Genetic Engineering | Article | By J.Smith</div></div>
    </div></article>
    <article class="card"><div class="card-head"><h2>Computation</h2><span class="see-all">SEE ALL</span></div><div class="body">
      <div class="fill f-calc" style="height:140px" role="img" aria-label="Hands working with a calculator and papers"></div>
      <div class="lead"><h3>Lorem ipsum dolor sit amet, consectetur adipiscing elit risus in magna varius commodo.</h3><div class="meta">Genetic Engineering | Article | By J.Smith</div></div>
      <div class="item"><p>Lorem ipsum dolor sit amet, consectetur adipiscing elit risus in magna varius commodo.</p><div class="meta">Genetic Engineering | Article | By J.Smith</div></div>
      <div class="item"><p>Lorem ipsum dolor sit amet, consectetur adipiscing elit risus in magna varius commodo.</p><div class="meta">Genetic Engineering | Article | By J.Smith</div></div>
    </div></article>
    <div style="padding-top:8px">
      <aside class="ad-host">
        <h4>HOST <span>UNLIMITED</span> WEBSITES</h4>
        <ul><li>UNLIMITED SPACE</li><li>UNLIMITED BANDWIDTH</li><li>24/7 SUPPORT</li><li>1 CLICK INSTALLS</li></ul>
        <div class="art" role="img" aria-label="Cartoon mascot"></div>
        <span class="click">CLICK HERE</span><span class="from">FROM ONLY</span><span class="price">$5.95</span>
      </aside>
      <aside class="ad-gig">
        <span class="tag">Free Trial</span>
        <h4>Outsource anything for a <span>fraction</span> of the cost!</h4>
        <div class="person" role="img" aria-label="Smiling professional at a laptop"></div>
        <div class="brand"><i></i>gigharbor.com</div>
      </aside>
    </div>
  </section>

  <!-- row 3 -->
  <section class="row" style="top:2120px;height:525px">
    <article class="card"><div class="card-head"><h2>Earth</h2><span class="see-all">SEE ALL</span></div><div class="body">
      <div class="fill f-earth" style="height:140px" role="img" aria-label="Globe held over a green field"></div>
      <div class="lead"><h3>Lorem ipsum dolor sit amet, consectetur adipiscing elit risus in magna varius commodo.</h3><div class="meta">Genetic Engineering | Article | By J.Smith</div></div>
      <div class="item"><p>Lorem ipsum dolor sit amet, consectetur adipiscing elit risus in magna varius commodo.</p><div class="meta">Genetic Engineering | Article | By J.Smith</div></div>
      <div class="item"><p>Lorem ipsum dolor sit amet, consectetur adipiscing elit risus in magna varius commodo.</p><div class="meta">Genetic Engineering | Article | By J.Smith</div></div>
    </div></article>
    <article class="card"><div class="card-head"><h2>Technology</h2><span class="see-all">SEE ALL</span></div><div class="body">
      <div class="fill f-tech" style="height:140px" role="img" aria-label="Devices connected in a glowing network"></div>
      <div class="lead"><h3>Lorem ipsum dolor sit amet, consectetur adipiscing elit risus in magna varius commodo.</h3><div class="meta">Genetic Engineering | Article | By J.Smith</div></div>
      <div class="item"><p>Lorem ipsum dolor sit amet, consectetur adipiscing elit risus in magna varius commodo.</p><div class="meta">Genetic Engineering | Article | By J.Smith</div></div>
      <div class="item"><p>Lorem ipsum dolor sit amet, consectetur adipiscing elit risus in magna varius commodo.</p><div class="meta">Genetic Engineering | Article | By J.Smith</div></div>
    </div></article>
    <article class="card"><div class="card-head"><h2>Recommended</h2><span class="see-all">SEE ALL</span></div><div class="body">
      <div class="mini"><div class="thumb fill t-grey" role="img" aria-label="Grey bacteria close-up"></div><div><p>Lorem ipsum dolor sit amet, consectetur adipiscing elit risus in magna...</p><div class="meta">Genetic Engineering | Article</div></div></div>
      <div class="mini"><div class="thumb fill t-insect" role="img" aria-label="Insect on a leaf"></div><div><p>Lorem ipsum dolor sit amet, consectetur adipiscing elit risus in magna...</p><div class="meta">Genetic Engineering | Article</div></div></div>
      <div class="mini"><div class="thumb fill t-red" role="img" aria-label="Red laboratory sample"></div><div><p>Lorem ipsum dolor sit amet, consectetur adipiscing elit risus in magna...</p><div class="meta">Genetic Engineering | Article</div></div></div>
      <div class="mini"><div class="thumb fill t-bench" role="img" aria-label="Researcher at a bench"></div><div><p>Lorem ipsum dolor sit amet, consectetur adipiscing elit risus in magna...</p><div class="meta">Genetic Engineering | Article</div></div></div>
    </div></article>
  </section>

  <!-- row 4 -->
  <section class="row" style="top:2673px;height:440px">
    <article class="card"><div class="card-head"><h2>Health</h2><span class="see-all">SEE ALL</span></div><div class="body">
      <div class="fill f-health" style="height:100px" role="img" aria-label="Medical staff at work in a clinic"></div>
      <div class="lead"><h3>Lorem ipsum dolor sit amet, consectetur adipiscing elit risus in magna varius commodo.</h3><div class="meta">Genetic Engineering | Article | By J.Smith</div></div>
      <div class="item"><p>Lorem ipsum dolor sit amet, consectetur adipiscing elit risus in magna varius commodo.</p><div class="meta">Genetic Engineering | Article | By J.Smith</div></div>
      <div class="item"><p>Lorem ipsum dolor sit amet, consectetur adipiscing elit risus in magna varius commodo.</p><div class="meta">Genetic Engineering | Article | By J.Smith</div></div>
    </div></article>
    <article class="card"><div class="card-head"><h2>Social</h2><span class="see-all">SEE ALL</span></div><div class="body">
      <div class="fill f-social" style="height:100px" role="img" aria-label="Hand-drawn social media word diagram"></div>
      <div class="lead"><h3>Lorem ipsum dolor sit amet, consectetur adipiscing elit risus in magna varius commodo.</h3><div class="meta">Genetic Engineering | Article | By J.Smith</div></div>
      <div class="item"><p>Lorem ipsum dolor sit amet, consectetur adipiscing elit risus in magna varius commodo.</p><div class="meta">Genetic Engineering | Article | By J.Smith</div></div>
      <div class="item"><p>Lorem ipsum dolor sit amet, consectetur adipiscing elit risus in magna varius commodo.</p><div class="meta">Genetic Engineering | Article | By J.Smith</div></div>
    </div></article>
    <article class="card"><div class="card-head"><h2>Others</h2><span class="see-all">SEE ALL</span></div><div class="body">
      <div class="fill f-tree" style="height:100px" role="img" aria-label="Colourful tree of icons illustration"></div>
      <div class="lead"><h3>Lorem ipsum dolor sit amet, consectetur adipiscing elit risus in magna varius commodo.</h3><div class="meta">Genetic Engineering | Article | By J.Smith</div></div>
      <div class="item"><p>Lorem ipsum dolor sit amet, consectetur adipiscing elit risus in magna varius commodo.</p><div class="meta">Genetic Engineering | Article | By J.Smith</div></div>
      <div class="item"><p>Lorem ipsum dolor sit amet, consectetur adipiscing elit risus in magna varius commodo.</p><div class="meta">Genetic Engineering | Article | By J.Smith</div></div>
    </div></article>
  </section>

  <!-- visit also -->
  <section class="band" style="top:3133px;height:400px">
    <div class="band-strip"></div>
    <div class="band-head"><span>VISIT ALSO</span><span class="arrows"><svg width="8" height="10" viewBox="0 0 8 10"><path d="M6 1 2 5l4 4" fill="none" stroke="#fff" stroke-width="2"/></svg><svg width="8" height="10" viewBox="0 0 8 10"><path d="M2 1l4 4-4 4" fill="none" stroke="#fff" stroke-width="2"/></svg></span></div>
    <div class="band-cards">
      <div class="band-card"><div class="fill f-lab" style="height:190px" role="img" aria-label="Laboratory equipment on a white bench"></div><h3>Lorem ipsum dolor sit amet, consectetur adipiscing elit risus in magna varius commodo.</h3><div class="strip"><div class="meta">Genetic Engineering | Article | By J.Smith</div></div></div>
      <div class="band-card"><div class="fill f-cells" style="height:190px" role="img" aria-label="Colourful fluorescent cell structures"></div><h3>Lorem ipsum dolor sit amet, consectetur adipiscing elit risus in magna varius commodo.</h3><div class="strip"><div class="meta">Genetic Engineering | Article | By J.Smith</div></div></div>
      <div class="band-card"><div class="fill f-worm" style="height:190px" role="img" aria-label="Grey microscope image of a worm"></div><h3>Lorem ipsum dolor sit amet, consectetur adipiscing elit risus in magna varius commodo.</h3><div class="strip"><div class="meta">Genetic Engineering | Article | By J.Smith</div></div></div>
      <div class="band-card"><div class="fill f-beetle" style="height:190px" role="img" aria-label="Close-up of a brown beetle"></div><h3>Lorem ipsum dolor sit amet, consectetur adipiscing elit risus in magna varius commodo.</h3><div class="strip"><div class="meta">Genetic Engineering | Article | By J.Smith</div></div></div>
    </div>
  </section>
</div>

<footer class="footer">
  <nav>ABOUT QLW<span>|</span>TERMS OF USE<span>|</span>PRIVACY POLICY<span>|</span>FOR ADVERTISERS<span>|</span>CONTACT US<span>|</span>FEEDBACK<span>|</span>HELP</nav>
  <p>Copyright © 2014 Quarry Lantern Works gGmbH<br>All rights reserved.</p>
</footer>
</body>
</html>
```